Bourbon Label Design For a Unique Craft Distillery

We are a craft distillery located in Mount Holly Nj looking for a label design for our new bourbon brand. The Name of the bourbon is going to be called "Iron Meadow" and the type of bourbon is a "straight Bourbon Whiskey". The First file are the pictures of our current brands. Would like the design to look Vintage but pop. The Bourbon will be a top shelf item. The Pictures of the other bottle are brands we like.

Target Market(s)

21-65 years old

Font styles to use
Decorative
Script

Colors
ec1f27
3176b5
1b1b1b
f5f5f5

Requirements
Must have
• vintage look, and pop !

```html
<!DOCTYPE html>
<html lang="en">
<head>
<meta charset="utf-8">
<title>Iron Meadow Straight Bourbon Whiskey – Label</title>
<link rel="stylesheet" href="https://fonts.googleapis.com/css2?family=Graduate&family=Pinyon+Script&family=Oswald:wght@500&display=swap">
<style>
  :root {
    --paper: #f5f5f5;
    --label-cream: #f1ecd8;
    --red: #ec1f27;
    --blue: #3176b5;
    --ink: #1b1b1b;
    --illustration: #5b4a33;
  }
  html, body {
    margin: 0;
    width: 1200px;
    height: 1200px;
    overflow: hidden;
    background: var(--paper);
  }
  .canvas {
    position: relative;
    width: 1200px;
    height: 1200px;
  }
  .front-label {
    position: absolute;
    left: 330px;
    top: 90px;
    width: 540px;
    height: 760px;
    background: var(--label-cream);
    color: var(--ink);
    box-sizing: border-box;
    border: 10px solid var(--red);
    outline: 3px solid var(--blue);
    outline-offset: -20px;
    padding: 40px 36px 24px;
    text-align: center;
  }
  .frame-curve { display: block; margin: 0 auto; }
  .brand-name {
    font-family: "Graduate", serif;
    font-size: 50px;
    letter-spacing: 2px;
    color: var(--red);
    margin: 0;
    line-height: 1;
    white-space: nowrap;
  }
  .emblem-row {
    display: flex;
    align-items: center;
    justify-content: space-between;
    margin-top: 14px;
    font-family: "Pinyon Script", cursive;
    font-size: 34px;
    color: var(--blue);
  }
  .train-illustration {
    width: 300px;
    height: 170px;
    border-radius: 150px 60px 20px 40px;
    background: linear-gradient(100deg, #3f3324, var(--illustration) 60%, #7a6547);
  }
  .distillery {
    font-family: "Graduate", serif;
    font-size: 44px;
    letter-spacing: 8px;
    margin: 12px 0 0;
    padding-bottom: 12px;
    border-bottom: 3px solid var(--blue);
  }
  .style-name {
    font-family: "Graduate", serif;
    font-size: 32px;
    margin: 18px 0 0;
    line-height: 1.1;
  }
  .style-name .script {
    font-family: "Pinyon Script", cursive;
    font-size: 48px;
    color: var(--red);
  }
  .style-name .star { font-size: 22px; vertical-align: middle; color: var(--blue); }
  .spec-table {
    margin: 22px auto 0;
    border-collapse: collapse;
    font-family: "Oswald", sans-serif;
    color: var(--ink);
  }
  .spec-table td {
    border: 2px solid var(--ink);
    padding: 2px 12px;
    min-width: 80px;
  }
  .spec-table .spec-head td { font-size: 11px; letter-spacing: 1px; background: var(--blue); color: var(--paper); }
  .spec-table .spec-value td { font-family: "Graduate", serif; font-size: 26px; }
  .origin {
    font-family: "Graduate", serif;
    font-size: 20px;
    letter-spacing: 6px;
    color: var(--red);
    margin: 16px 0 0;
  }
  .neck-strip {
    position: absolute;
    left: 200px;
    top: 980px;
    width: 800px;
    height: 96px;
    background: var(--label-cream);
    border-top: 4px solid var(--red);
    border-bottom: 4px solid var(--red);
    color: var(--red);
    font-family: "Graduate", serif;
    font-size: 34px;
    letter-spacing: 3px;
    display: flex;
    align-items: center;
    justify-content: space-between;
    padding: 0 24px;
    box-sizing: border-box;
  }
  .neck-strip .mirrored { transform: rotate(180deg); }
  .neck-seal {
    position: absolute;
    left: 50%;
    top: 50%;
    width: 160px;
    height: 160px;
    margin: -80px 0 0 -80px;
    border-radius: 50%;
    background: var(--label-cream);
    border: 4px solid var(--blue);
    box-sizing: border-box;
    display: flex;
    align-items: center;
    justify-content: center;
  }
  .neck-seal .train-illustration {
    width: 120px;
    height: 66px;
    border-radius: 60px 30px 10px 20px;
  }
</style>
</head>
<body>
<main class="canvas">
  <section class="front-label">
    <svg class="frame-curve" width="448" height="36" viewBox="0 0 448 36">
      <path d="M4 32 Q224 -6 444 32" fill="none" stroke="#3176b5" stroke-width="3"/>
    </svg>
    <h1 class="brand-name">IRON MEADOW</h1>
    <svg class="frame-curve" width="448" height="26" viewBox="0 0 448 26">
      <path d="M4 4 Q224 30 444 4" fill="none" stroke="#3176b5" stroke-width="3"/>
    </svg>
    <div class="emblem-row">
      <span class="est">Est.</span>
      <div class="train-illustration" role="img" aria-label="Engraved illustration of a streamlined vintage locomotive front"></div>
      <span class="year">2018</span>
    </div>
    <h2 class="distillery">DISTILLERY</h2>
    <p class="style-name">STRAIGHT BOURBON<br><span class="star">★</span> <span class="script">Whiskey</span> <span class="star">★</span></p>
    <table class="spec-table">
      <tr class="spec-head"><td>BATCH NO</td><td>VOLUME</td><td>ALC VOL</td><td>PROOF</td></tr>
      <tr class="spec-value"><td>007</td><td>750ML</td><td>43%</td><td>86</td></tr>
    </table>
    <p class="origin">CEDAR HOLLOW, NJ</p>
  </section>

  <section class="neck-strip">
    <span class="strip-name">IRON MEADOW</span>
    <span class="strip-name mirrored">IRON MEADOW</span>
    <div class="neck-seal">
      <div class="train-illustration" role="img" aria-label="Small engraved locomotive illustration"></div>
    </div>
  </section>
</main>
</body>
</html>
```